nonprofit organization looking for sleek new design

We need a fresh new look for this nonprofit organization, Tidewater Allies for Learning and Mutual Aid, INC (TALMA, Inc.). This organization provides educational, nutritional, dental health, and specialized services to Cedar Step children, aiming to support families meeting federal income poverty guidelines. Our mission is clear: "Creating a brighter future for the children and la familia." We focus on child development, family wellness, staff growth, and community partnerships.

```html
<!DOCTYPE html>
<html lang="en">
<head>
<meta charset="utf-8">
<title>TALMA, Inc. — Creating a brighter future</title>
<link href="https://fonts.googleapis.com/css2?family=Montserrat:wght@400;500;600;700;800&display=swap" rel="stylesheet">
<style>
:root{
  --navy:#0b4ea2;
  --navy-dark:#0a3f8a;
  --orange:#f7941d;
  --orange-deep:#f26f21;
  --sky:#12aef5;
  --ice:#e6f2fc;
  --ink:#1d1d1f;
  --text:#55585e;
  --mist:#f5f5f5;
  --white:#ffffff;
}
*{box-sizing:border-box;margin:0;padding:0}
html,body{width:1200px;height:5254px;overflow:hidden}
body{font-family:"Montserrat",sans-serif;color:var(--text);background:var(--white);position:relative}
.section{position:absolute;left:0;width:1200px;overflow:hidden}
.abs{position:absolute}
.photo{position:absolute}
.eyebrow{font-size:13px;letter-spacing:1.5px;color:var(--orange);text-transform:uppercase;font-weight:500}
.title{font-size:31px;font-weight:700;color:var(--navy);text-transform:uppercase;line-height:1.15}
.rule{width:50px;height:3px;background:var(--orange)}
.copy{font-size:14px;line-height:22px;color:var(--text)}
.btn{position:absolute;display:flex;align-items:center;justify-content:center;border-radius:22px;font-size:11px;font-weight:700;letter-spacing:1px;color:var(--white);text-transform:uppercase}
.btn-navy{background:var(--navy)}
.btn-orange{background:var(--orange)}
.center{left:0;width:1200px;text-align:center}

/* header + hero */
.hero{top:0;height:700px}
.hero-photo{inset:0;background:linear-gradient(110deg,#e9e3dc 0%,#d9cdbf 35%,#c9b7a4 55%,#e3ddd6 75%,#f0ece7 100%)}
.brand{position:absolute;left:94px;top:26px;display:flex;align-items:center;gap:10px;font-size:27px;font-weight:700;color:var(--navy)}
.brand-dot{width:26px;height:26px;border-radius:50%;background:var(--sky)}
.nav{position:absolute;top:28px;left:370px;display:flex;font-size:12px;color:var(--navy)}
.nav a{position:absolute;white-space:nowrap;text-decoration:none;color:var(--navy)}
.nav .active{color:var(--orange)}
.nav .active::after{content:"";position:absolute;left:8px;right:8px;bottom:-8px;height:2px;background:var(--orange)}
.nav-cta{position:absolute;left:938px;top:20px;width:139px;height:35px;border-radius:18px;background:var(--navy-dark);color:var(--white);font-size:12px;display:flex;align-items:center;justify-content:center}
.hero-circle{position:absolute;left:120px;top:147px;width:430px;height:430px;border-radius:50%;background:radial-gradient(circle at 40% 30%,#ffb03b,var(--orange) 55%,var(--orange-deep));box-shadow:0 0 0 6px rgba(255,255,255,.55);text-align:center;color:var(--white)}
.hero-circle h1{margin-top:118px;font-size:32px;line-height:39px;font-weight:700;text-transform:uppercase}
.hero-circle h1 span{font-weight:400;display:block}
.hero-dots{left:34px;top:313px}
.hero-dots i{display:block;width:13px;height:13px;border-radius:50%;border:2px solid var(--sky);margin-bottom:17px}
.hero-dots i.on{background:var(--navy);border-color:var(--navy)}
.scroll{left:1130px;top:330px;transform:rotate(-90deg);transform-origin:left top;font-size:10px;letter-spacing:2px;color:var(--white)}

/* about */
.about{top:700px;height:612px}
.about-photo{left:92px;top:136px;width:479px;height:409px;background:linear-gradient(180deg,#f4f4f4,#ececec);border-radius:6px}
.about h3{font-size:19px;line-height:27px;color:var(--ink);font-weight:600}

/* services */
.services{top:1312px;height:684px;background:linear-gradient(90deg,#f3f8fd,var(--ice) 60%,#d9ebfa)}
.family-photo{left:75px;top:269px;width:455px;height:415px;background:linear-gradient(160deg,#c9a88f,#a47b60 50%,#e8d6c8);border-radius:60px 60px 0 0}
.card{position:absolute;background:var(--white);border-radius:30px 30px 30px 30px;box-shadow:0 12px 30px rgba(11,78,162,.12);padding:0 26px}
.card-blue{background:linear-gradient(150deg,#1a73d6,var(--navy-dark));color:var(--white)}
.card svg{display:block}
.card h4{font-size:17px;font-weight:500;color:var(--navy);text-transform:uppercase;line-height:20px;border-left:2px solid var(--navy);padding-left:0;margin-left:-26px;padding-left:24px}
.card-blue h4{color:var(--white);border-color:transparent}
.card p{font-size:10.5px;line-height:18px;color:var(--text);margin-top:8px}
.card-blue p{color:#dfeaf8}
.card .more{display:block;font-size:9px;font-weight:700;color:var(--navy);margin-top:10px}
.card-blue .more{color:var(--white)}

/* development */
.develop{top:1996px;height:596px}
.dev-frame{left:131px;top:82px;width:463px;height:440px;border:6px solid var(--orange);border-left:none;border-top:none;border-radius:0 190px 0 60px}
.dev-photo{left:120px;top:71px;width:462px;height:440px;background:linear-gradient(140deg,#e7dcd4,#cdb3a2 45%,#aebfd8 80%,#efe9e4);border-radius:0 190px 0 60px}

/* community */
.community{top:2592px;height:561px;background:var(--mist)}
.comm-block{left:573px;top:66px;width:400px;height:286px;background:var(--sky);border-radius:4px}
.comm-photo{left:596px;top:84px;width:510px;height:368px;background:radial-gradient(circle at 45% 55%,#6f6c69,#9a948e 35%,#e9e6e2 70%);border-radius:10px}

/* testimonial */
.wellness{top:3153px;height:490px}
.wellness-photo{left:0;top:0;width:596px;height:490px;background:linear-gradient(180deg,#b9d8e8 0%,#8fb77a 45%,#6d9a4f 75%,#8cbf5e 100%)}
.wellness-panel{left:596px;top:0;width:604px;height:490px;background:var(--sky);text-align:center;color:var(--white)}
.wellness-arc{left:470px;top:340px;width:260px;height:260px;border-radius:50%;background:#3ec0f8}

/* blogs */
.blogs{top:3643px;height:592px}
.post-photo{position:absolute;top:166px;width:284px;height:200px}
.post{position:absolute;top:331px;width:255px;height:184px;background:var(--white);box-shadow:0 8px 22px rgba(0,0,0,.08);padding:18px 22px}
.pill{display:inline-block;background:var(--navy-dark);color:var(--white);font-size:8px;border-radius:9px;padding:3px 12px}
.post h5{font-size:11px;line-height:15px;color:var(--ink);font-weight:600;margin-top:9px}
.post p{font-size:8.5px;line-height:14px;margin-top:9px}
.post .more{font-size:8px;font-weight:700;color:var(--navy);margin-top:8px;display:block}

/* call to action */
.cta{top:4235px;height:591px}
.cta-photo{left:0;top:0;width:900px;height:591px;background:linear-gradient(90deg,#dcc5ad 0%,#c98f55 35%,#d9b08a 60%,rgba(255,255,255,0) 100%)}
.cta-box{left:584px;top:102px;width:506px;height:325px;background:linear-gradient(120deg,var(--orange),#f9a43c);color:var(--white);padding:0 60px}
.cta-box h2{margin-top:58px;font-size:25px;line-height:32px;font-weight:600;text-transform:uppercase}
.cta-box p{margin-top:18px;font-size:13.5px;line-height:24px;color:#fff3e2}
.btn-ghost{border:2px solid var(--white);background:transparent}

/* footer */
.footer{top:4826px;height:428px}
.foot-brand{left:129px;top:88px;font-size:27px;color:var(--sky);font-weight:500}
.social{top:143px;width:31px;height:31px;border:2px solid var(--sky);border-radius:50%}
.divider{top:0;width:1px;height:275px;background:#e3e3e3}
.foot-col h6{font-size:15px;font-weight:600;color:var(--ink);text-transform:uppercase;border-left:3px solid var(--orange);padding-left:12px;margin-left:-15px}
.foot-col li{list-style:none;font-size:12px;color:var(--text);margin-top:16px}
.contact-row{position:absolute;left:0;display:flex;gap:12px;font-size:12px;line-height:16px}
.contact-row small{display:block;font-size:11px;color:var(--text)}
.contact-row b{font-weight:500;color:var(--ink);font-size:13px}
.bottom-line{left:0;top:330px;width:1200px;height:1px;background:#e3e3e3}
.copyright{top:366px;font-size:12px;color:var(--text)}
</style>
</head>
<body>

<header class="section hero">
  <div class="photo hero-photo" role="img" aria-label="Photo of a smiling teacher with a clipboard beside a young boy building with colourful toy blocks"></div>
  <div class="brand"><span class="brand-dot"></span>TALMA, Inc.</div>
  <nav class="nav">
    <a class="active" style="left:0">HOME</a>
    <a style="left:101px">ABOUT US</a>
    <a style="left:226px">SERVICES</a>
    <a style="left:348px">WHY US?</a>
    <a style="left:466px">BLOGS</a>
  </nav>
  <a class="nav-cta">CONTACT US</a>
  <div class="abs hero-dots"><i></i><i class="on"></i><i></i></div>
  <div class="abs scroll">‹ SCROLL DOWN</div>
  <div class="hero-circle">
    <h1>Creating a<br>brighter future<span>for the children<br>and la familia</span></h1>
    <a class="btn btn-navy" style="left:133px;top:288px;width:157px;height:40px">Learn more</a>
  </div>
</header>

<section class="section about">
  <p class="abs eyebrow center" style="top:63px">Who we are</p>
  <h2 class="abs title center" style="top:84px">About TALMA</h2>
  <div class="abs rule" style="left:575px;top:128px"></div>
  <div class="photo about-photo" role="img" aria-label="Photo of five children peeking over and around a large white sign bearing the organisation's name"></div>
  <div class="abs" style="left:620px;top:204px;width:480px">
    <h3>Lorem ipsum dolor sit amet, consectetur adipiscing elit sed do eiusmod</h3>
    <p class="copy" style="margin-top:20px">Alabore et dolore magna aliqua. Ut enim ad minim veniam, quis nostrud exercitation ullamco laboris nisi ut aliquip ex</p>
    <p class="copy" style="margin-top:22px">Duis aute irure dolor in reprehenderit in voluptate velit esse cillum dolore eu fugiat nulla pariatur. Excepteur sint occaecat cupidatat non proident, sunt in culpa qui officia deserunt mollit animr in reprehenderit .</p>
  </div>
  <a class="btn btn-navy" style="left:620px;top:475px;width:158px;height:41px">Learn more</a>
</section>

<section class="section services">
  <p class="abs eyebrow" style="left:124px;top:112px">Services</p>
  <h2 class="abs title" style="left:124px;top:138px">What we do</h2>
  <div class="abs rule" style="left:124px;top:185px;width:70px"></div>
  <p class="abs copy" style="left:127px;top:202px;width:330px">Alabore et dolore magna aliqua. Ut enim ad minim veniam, quis nostrud exercitation</p>
  <svg class="abs" style="left:290px;top:260px" width="210" height="110" viewBox="0 0 210 110" fill="none"><path d="M4 20 C60 60 120 70 130 40 C140 10 110 5 108 30 C106 60 160 90 200 96" stroke="#0b4ea2" stroke-width="1.5" stroke-dasharray="4 4"/><path d="M192 90 l12 7 -13 3z" fill="#0b4ea2"/></svg>
  <div class="photo family-photo" role="img" aria-label="Photo of a laughing family of four with a child riding on his father's shoulders"></div>

  <div class="card card-blue" style="left:514px;top:65px;width:257px;height:231px;border-radius:40px 40px 6px 40px">
    <svg style="margin-top:36px" width="44" height="34" viewBox="0 0 44 34" fill="none" stroke="#fff" stroke-width="2"><path d="M2 12 22 3l20 9-20 9z"/><path d="M10 16v9c6 5 18 5 24 0v-9"/><path d="M40 13v12"/></svg>
    <h4 style="margin-top:12px">Educational</h4>
    <p>Duis aute irure dolor in repreh enderit in voluptate velit esse cillum dolore eu fugiat n</p>
    <span class="more">LEARN MORE</span>
  </div>
  <div class="card" style="left:798px;top:128px;width:259px;height:233px;border-radius:40px 40px 40px 6px">
    <svg style="margin-top:22px;margin-left:8px" width="54" height="52" viewBox="0 0 54 52" fill="none" stroke="#f7941d" stroke-width="2"><path d="M18 10c-6-4-14 0-13 8 1 7 4 10 5 20 1 6 6 6 7 0l2-8 2 8c1 6 6 6 7 0 1-10 4-13 5-20 1-8-7-12-13-8"/><path d="M38 6l10-4M40 14l12 2"/></svg>
    <h4 style="margin-top:10px">Dental health</h4>
    <p>Duis aute irure dolor in repreh enderit in voluptate velit esse cillum dolore eu fugiat n</p>
    <span class="more">LEARN MORE</span>
  </div>
  <div class="card" style="left:526px;top:322px;width:257px;height:231px;border-radius:40px 40px 6px 40px">
    <svg style="margin-top:22px" width="50" height="48" viewBox="0 0 50 48" fill="none" stroke="#f7941d" stroke-width="2"><rect x="4" y="18" width="18" height="26" rx="3"/><path d="M8 18v-6h10v6"/><circle cx="34" cy="32" r="12"/><path d="M34 20c0-6 4-10 10-10"/></svg>
    <h4 style="margin-top:10px">Nutritional</h4>
    <p>Duis aute irure dolor in repreh enderit in voluptate velit esse cillum dolore eu fugiat n</p>
    <span class="more">LEARN MORE</span>
  </div>
  <div class="card" style="left:808px;top:379px;width:257px;height:231px;border-radius:40px 40px 40px 6px">
    <svg style="margin-top:24px" width="50" height="50" viewBox="0 0 50 50" fill="none" stroke="#f7941d" stroke-width="2"><circle cx="25" cy="12" r="6"/><path d="M14 30c0-7 5-11 11-11s11 4 11 11"/><circle cx="10" cy="30" r="4"/><circle cx="40" cy="30" r="4"/><path d="M4 46c0-5 3-8 6-8s6 3 6 8M34 46c0-5 3-8 6-8s6 3 6 8"/></svg>
    <h4 style="margin-top:8px">Specialized<br>services</h4>
    <p>Duis aute irure dolor in repreh enderit in voluptate velit</p>
    <span class="more">LEARN MORE</span>
  </div>
</section>

<section class="section develop">
  <div class="abs dev-frame"></div>
  <div class="photo dev-photo" role="img" aria-label="Photo of a smiling mother and her young daughter playing with a bead abacus"></div>
  <p class="abs eyebrow" style="left:677px;top:175px">Child education &amp; develop</p>
  <h2 class="abs title" style="left:683px;top:202px;font-size:26px">Child development</h2>
  <p class="abs copy" style="left:688px;top:271px;width:370px">Alabore et dolore magna aliqua. Ut enim ad minim veniam, quis nostrud exercitation ullamco laboris nisi ut aliquip ex Alabore et dolore magna aliqua. Ut enim ad minim veniam, quis nostrud.</p>
  <a class="btn btn-navy" style="left:688px;top:388px;width:157px;height:40px">Learn more</a>
</section>

<section class="section community">
  <p class="abs eyebrow" style="left:129px;top:102px">Lorem ipsum dolor sit</p>
  <h2 class="abs title" style="left:131px;top:129px;font-size:30px">Community<br>partnersihp</h2>
  <div class="abs rule" style="left:135px;top:216px;width:80px"></div>
  <p class="abs copy" style="left:135px;top:243px;width:370px">Alabore et dolore magna aliqua. Ut enim ad minim veniam, quis nostrud exercitation ullamco laboris nisi ut aliquip ex Alabore et dolore magna aliqua. Ut enim ad minim veniam, quis nostrud.</p>
  <a class="btn btn-orange" style="left:135px;top:358px;width:158px;height:40px">Learn more</a>
  <div class="abs comm-block"></div>
  <div class="photo comm-photo" role="img" aria-label="Photo of a diverse group of adults joining hands in a circle, seen from above"></div>
</section>

<section class="section wellness">
  <div class="photo wellness-photo" role="img" aria-label="Photo of a joyful family with arms outstretched in a sunny park"></div>
  <div class="abs wellness-panel">
    <div class="abs wellness-arc"></div>
    <p style="margin-top:91px;font-size:12px;letter-spacing:1.5px;text-transform:uppercase">Testimonials</p>
    <h2 style="margin-top:8px;font-size:29px;font-weight:700;text-transform:uppercase">Family wellness</h2>
    <p style="margin:24px auto 0;width:370px;font-size:15px;line-height:26px;font-weight:700;color:#fff6cc">Lorem ipsum dolor sit amet, consectetur adipiscing elit, sed do eiusmo</p>
    <p style="margin:14px auto 0;width:420px;font-size:14px;line-height:26px;color:#eef9ff">ut labore et dolore magna aliqua. Ut enim ad minim veniam, quis nostrud exercitation ullamco laboris nisi ut aliquip ex ea commodo consequat. Duis</p>
    <a class="btn btn-orange" style="left:216px;top:344px;width:155px;height:37px">Learn more</a>
  </div>
</section>

<section class="section blogs">
  <p class="abs eyebrow center" style="top:56px">Article &amp; blogs</p>
  <h2 class="abs title center" style="top:86px">Latest blogs</h2>
  <div class="abs rule" style="left:565px;top:130px;width:70px"></div>

  <div class="post-photo" style="left:149px;background:linear-gradient(120deg,#d8d4cf,#b9a596 50%,#8b8f96)" role="img" aria-label="Photo of a woman and a man smiling together in an office"></div>
  <div class="post-photo" style="left:469px;background:linear-gradient(180deg,#f4f7f4,#b7c9a8 40%,#b78450 80%)" role="img" aria-label="Photo of a green plant growing from a glass jar of coins"></div>
  <div class="post-photo" style="left:781px;background:linear-gradient(120deg,#cfc7bd,#a9907d 50%,#e4e0da)" role="img" aria-label="Photo of two colleagues laughing in a bright workspace"></div>

  <article class="post" style="left:163px"><span class="pill">18 JAN 2022</span><h5>Lorem ipsum dolor sit amet consectetur adipiscing</h5><p>Sed ut perspiciatis unde omnis iste natus error sit voluptatem accusantium doloremque laudantium</p><span class="more">LEARN MORE</span></article>
  <article class="post" style="left:481px"><span class="pill">18 JAN 2022</span><h5>Lorem ipsum dolor sit amet consectetur adipiscing</h5><p>Sed ut perspiciatis unde omnis iste natus error sit voluptatem accusantium doloremque laudantium</p><span class="more">LEARN MORE</span></article>
  <article class="post" style="left:794px"><span class="pill">18 JAN 2022</span><h5>Lorem ipsum dolor sit amet consectetur adipiscing</h5><p>Sed ut perspiciatis unde omnis iste natus error sit voluptatem accusantium doloremque laudantium</p><span class="more">LEARN MORE</span></article>
</section>

<section class="section cta">
  <div class="photo cta-photo" role="img" aria-label="Photo of a mother in glasses helping her young daughter write in a notebook"></div>
  <div class="abs cta-box">
    <h2>Start building your<br>child bright future</h2>
    <p>Lorem ipsum dolor sit amet, consectetur adipiscing elit, sed do eiusmod tempor incididunt ut labore et dolore magna aliqua. Ut enim ad minim</p>
    <a class="btn btn-ghost" style="left:59px;top:229px;width:154px;height:40px">Contact us</a>
  </div>
</section>

<footer class="section footer">
  <div class="abs foot-brand">TALMA, INC</div>
  <span class="abs social" style="left:160px"></span>
  <span class="abs social" style="left:199px"></span>
  <span class="abs social" style="left:238px"></span>

  <div class="abs divider" style="left:351px"></div>
  <div class="abs divider" style="left:606px"></div>
  <div class="abs divider" style="left:822px"></div>

  <div class="abs foot-col" style="left:378px;top:84px">
    <h6>Navigation</h6>
    <ul style="margin-top:8px"><li>About Us</li><li>The Community</li><li>Programs</li><li>News</li><li>Services</li></ul>
  </div>
  <div class="abs foot-col" style="left:633px;top:84px">
    <h6>Resources</h6>
    <ul style="margin-top:8px"><li>Blogs</li><li>Support Us</li><li>Contact Us</li><li>Privacy Policy</li></ul>
  </div>
  <div class="abs foot-col" style="left:853px;top:84px;width:330px;height:200px">
    <h6>Contact us</h6>
    <div class="contact-row" style="top:44px">
      <svg width="18" height="18" viewBox="0 0 24 24" fill="#0b4ea2"><path d="M6.6 10.8a15 15 0 0 0 6.6 6.6l2.2-2.2a1 1 0 0 1 1-.25 11.4 11.4 0 0 0 3.6.57 1 1 0 0 1 1 1V20a1 1 0 0 1-1 1A17 17 0 0 1 3 4a1 1 0 0 1 1-1h3.5a1 1 0 0 1 1 1c0 1.25.2 2.45.57 3.6a1 1 0 0 1-.25 1z"/></svg>
      <div><small>Phone</small><b>04-5580372</b></div>
    </div>
    <div class="contact-row" style="top:94px">
      <svg width="18" height="20" viewBox="0 0 24 24" fill="#0b4ea2"><path d="M12 2a7 7 0 0 0-7 7c0 5.25 7 13 7 13s7-7.75 7-13a7 7 0 0 0-7-7zm0 9.5A2.5 2.5 0 1 1 12 6.5a2.5 2.5 0 0 1 0 5z"/></svg>
      <div><small>Office</small><b>Harbor Row 12/4 POB 2210 Bayfield, 41760</b></div>
    </div>
    <div class="contact-row" style="top:146px">
      <svg width="18" height="16" viewBox="0 0 24 20" fill="#0b4ea2"><path d="M2 2h20v16H2z" fill="none" stroke="#0b4ea2" stroke-width="2"/><path d="M2 3l10 8 10-8" fill="none" stroke="#0b4ea2" stroke-width="2"/></svg>
      <div><small>Email</small><b>info@talma.org</b></div>
    </div>
  </div>

  <div class="abs bottom-line"></div>
  <p class="abs copyright center">Copyright © 2024 Tidewater Allies for Learning and Mutual Aid, INC</p>
</footer>

</body>
</html>
```